Orbit Hopperz VR is the name of our project, We are a Virtual Reality Theme park

We need a web page and logo that is sharp and exciting, and futuristic that people would want to have on a tee shirt.. We like teal -black- silver colour. Customers will be able to book on line- we will have Free Roam VR experiences , Strydex(treadmills), Stand alone VR stations and VR Simulator rides.

Logo Text

Orbit Hopperz VR

```html
<!DOCTYPE html>
<html lang="en">
<head>
<meta charset="utf-8">
<title>Orbit Hopperz VR</title>
<link href="https://fonts.googleapis.com/css2?family=Nunito+Sans:wght@400;600;700;800&display=swap" rel="stylesheet">
<style>
:root{
  --teal:#0f8584;
  --teal-dark:#0b6f6e;
  --ink:#151515;
  --text:#333;
  --muted:#555;
  --white:#fff;
  --footer:#1b1b1b;
  --footer-bar:#121212;
  --rule:#e6e6e6;
}
*{margin:0;padding:0;box-sizing:border-box}
html,body{width:1200px;height:3488px;overflow:hidden}
body{font-family:"Nunito Sans",sans-serif;color:var(--text);background:var(--white);position:relative}
.abs{position:absolute}
/* header */
.header{left:0;top:0;width:1200px;height:110px;background:var(--white)}
.brand-dot{left:114px;top:20px;width:72px;height:72px;border-radius:50%;background:var(--teal)}
.brand-name{left:200px;top:34px;font-size:30px;font-weight:800;color:var(--ink)}
.nav{left:576px;top:44px;display:flex;gap:20px;font-size:17px;color:var(--ink);white-space:nowrap}
.search{left:1064px;top:42px}
/* hero */
.hero{left:0;top:110px;width:1200px;height:558px;background:linear-gradient(100deg,#3a2a2e 0%,#6b4a4a 35%,#8a5a55 55%,#4a3036 80%,#2e2226 100%)}
.hero-kicker{left:114px;top:244px;font-size:27px;font-weight:600;color:var(--white)}
.hero-title{left:110px;top:286px;font-size:56px;font-weight:800;color:var(--white);white-space:nowrap}
.hero-text{left:114px;top:370px;width:520px;font-size:17px;line-height:28px;color:var(--white)}
.btn-solid{background:var(--teal);color:var(--white);font-weight:700;display:flex;align-items:center;justify-content:center}
.hero-btn{left:114px;top:447px;width:179px;height:49px;font-size:18px}
.dot{width:10px;height:10px;border-radius:50%;background:var(--white);left:1141px}
.dot-active{left:1136px;width:20px;height:20px;border:2px solid var(--white);background:transparent;display:flex;align-items:center;justify-content:center}
.dot-active::after{content:"";width:10px;height:10px;border-radius:50%;background:var(--white)}
/* about */
.about-photo{left:163px;top:777px;width:421px;height:530px;background:linear-gradient(160deg,#e9e6e2 0%,#d9c7a8 45%,#d9a421 70%,#c58d14 100%)}
.play-box{left:163px;top:1191px;width:116px;height:116px;background:var(--teal);outline:10px solid var(--white);display:flex;align-items:center;justify-content:center}
.about-card{left:584px;top:777px;width:435px;height:530px;background:var(--white);box-shadow:0 6px 18px rgba(0,0,0,.15)}
.about-label{left:657px;top:810px;font-size:18px;font-weight:700;color:var(--teal)}
.about-title{left:657px;top:851px;width:320px;font-size:39px;line-height:48px;font-weight:800;color:var(--ink)}
.rule{height:3px;background:var(--teal)}
.about-rule{left:659px;top:1060px;width:56px}
.about-text{left:658px;top:1098px;width:300px;font-size:16px;line-height:26px;color:var(--muted)}
.about-btn{left:658px;top:1219px;width:161px;height:51px;font-size:18px}
/* offer */
.center{left:0;width:1200px;text-align:center}
.section-title{font-size:39px;font-weight:800}
.offer-title{top:1450px;color:var(--teal)}
.offer-rule{left:570px;top:1512px;width:60px}
.offer{width:190px;text-align:center;top:1580px}
.offer svg{display:block;margin:0 auto 18px}
.offer-label{font-size:21px;line-height:31px;font-weight:700;color:#444}
.offer.active .offer-label{color:var(--teal)}
.offer-underline{left:516px;top:1778px;width:170px;height:4px;background:var(--teal)}
/* games */
.games{left:0;top:1895px;width:1200px;height:626px;background:var(--teal)}
.games-kicker{top:1958px;font-size:18px;color:var(--white)}
.games-title{top:1986px;color:var(--white)}
.games-rule{left:570px;top:2054px;width:60px;background:var(--white)}
.game{top:2116px;width:247px;text-align:center}
.game-photo{height:235px}
.game-name{margin-top:24px;font-size:20px;font-weight:800;color:var(--white)}
.book{margin:14px auto 0;width:128px;height:40px;border:2px solid var(--white);color:var(--white);font-size:15px;font-weight:700;display:flex;align-items:center;justify-content:center}
/* testimonials */
.t-label{top:2614px;font-size:18px;font-weight:700;color:var(--teal)}
.t-title{top:2651px;color:var(--ink);font-size:40px}
.t-rule{left:570px;top:2726px;width:60px}
.t-text{left:320px;width:560px;top:2760px;font-size:20px;line-height:30px;text-align:center;color:var(--text)}
.t-name{top:2836px;font-size:20px;font-weight:800;color:var(--ink)}
.avatar{top:2888px;width:49px;height:49px;background:linear-gradient(160deg,#b89a80,#6e5444)}
.avatar.active{outline:3px solid var(--teal);outline-offset:-3px}
/* footer */
.footer{left:0;top:3023px;width:1200px;height:386px;background:var(--footer);color:var(--white)}
.f-logo{left:191px;top:3135px;width:116px;height:116px;border-radius:50%;background:var(--white)}
.f-name{left:0;width:498px;top:3272px;text-align:center;font-size:25px;font-weight:800;color:var(--white)}
.f-head{top:3104px;font-size:23px;font-weight:800;color:var(--white)}
.f-links{left:539px;top:3153px;list-style:none;font-size:16px;line-height:31px;color:var(--white)}
.f-contact{left:849px;top:3160px;font-size:16px;color:var(--white)}
.f-contact div{display:flex;gap:14px;margin-bottom:11px;line-height:23px}
.f-contact svg{flex:none;margin-top:5px}
.footbar{left:0;top:3409px;width:1200px;height:79px;background:var(--footer-bar)}
.copy{left:116px;top:3436px;font-size:15px;color:var(--white)}
.social{top:3439px;width:18px;height:18px;border-radius:50%;background:var(--white)}
</style>
</head>
<body>

<header class="abs header">
  <div class="abs brand-dot"></div>
  <div class="abs brand-name">Orbit Hopperz VR</div>
  <nav class="abs nav"><span>Home</span><span>About</span><span>Games</span><span>Blog</span><span>Testimonials</span><span>Contacts</span></nav>
  <svg class="abs search" width="24" height="24" viewBox="0 0 24 24"><circle cx="10" cy="10" r="7" fill="none" stroke="#0f8584" stroke-width="2.5"/><line x1="15" y1="15" x2="22" y2="22" stroke="#0f8584" stroke-width="2.5"/></svg>
</header>

<section class="abs hero" role="img" aria-label="Person wearing a VR headset at a theme park at night"></section>
<div class="abs hero-kicker">Welcome to</div>
<h1 class="abs hero-title">Orbit Hopperz VR</h1>
<p class="abs hero-text">Ut enim ad minima veniam, quis nostrum exercitationem ullam corporis suscipit laboriosam, nisi ut aliquid ex ea</p>
<div class="abs btn-solid hero-btn">LEARN MORE</div>
<div class="abs dot dot-active" style="top:360px"></div>
<div class="abs dot" style="top:395px"></div>
<div class="abs dot" style="top:427px"></div>

<div class="abs about-photo" role="img" aria-label="Woman in a yellow sweater wearing a VR headset"></div>
<div class="abs play-box"><svg width="66" height="66" viewBox="0 0 66 66"><circle cx="33" cy="33" r="30" fill="none" stroke="#fff" stroke-width="2.5"/><path d="M26 20 L46 33 L26 46 Z" fill="none" stroke="#fff" stroke-width="2.5" stroke-linejoin="round"/></svg></div>
<div class="abs about-card"></div>
<div class="abs about-label">About The Orbit Hopperz VR</div>
<h2 class="abs about-title">Nam libero tempore, cum soluta nobis est eligendi</h2>
<div class="abs rule about-rule"></div>
<p class="abs about-text">Ut enim ad minima veniam, quis nostrum exercitationem ullam corporis suscipit laboriosam, nisi ut aliquid ex ea commodi consequatur</p>
<div class="abs btn-solid about-btn">Learn More</div>

<h2 class="abs center section-title offer-title">What We Offer</h2>
<div class="abs rule offer-rule"></div>
<div class="abs offer" style="left:126px;top:1588px">
  <svg width="80" height="56" viewBox="0 0 80 56" fill="none" stroke="#444" stroke-width="2"><text x="14" y="30" font-family="Nunito Sans,sans-serif" font-size="20" font-weight="700" fill="#444" stroke="none">360°</text><ellipse cx="40" cy="30" rx="36" ry="14"/></svg>
  <div class="offer-label">360 Viewing<br>Angle</div>
</div>
<div class="abs offer" style="left:314px">
  <svg width="60" height="70" viewBox="0 0 60 70" fill="none" stroke="#444" stroke-width="2"><circle cx="30" cy="9" r="6"/><path d="M22 20h16v20h-16z M26 40v16 M34 40v16 M8 62h44 M14 58l-6 4 6 4 M46 58l6 4-6 4"/></svg>
  <div class="offer-label">Effect of<br>Presence</div>
</div>
<div class="abs offer active" style="left:505px">
  <svg width="60" height="70" viewBox="0 0 60 70" fill="none" stroke="#0f8584" stroke-width="2"><path d="M10 36 C10 12 50 12 50 36 L50 52 C50 62 10 62 10 52 Z"/><rect x="12" y="34" width="36" height="14" rx="5"/></svg>
  <div class="offer-label">Extra Comfort<br>for Head</div>
</div>
<div class="abs offer" style="left:700px">
  <svg width="80" height="70" viewBox="0 0 80 70" fill="none" stroke="#444" stroke-width="2"><rect x="12" y="22" width="56" height="30" rx="8"/><rect x="18" y="12" width="20" height="12" rx="3"/><path d="M30 42l12-10 M38 44l10-8"/></svg>
  <div class="offer-label">Easy Operation<br>System</div>
</div>
<div class="abs offer" style="left:889px">
  <svg width="80" height="70" viewBox="0 0 80 70" fill="none" stroke="#444" stroke-width="2"><path d="M28 14 Q40 4 52 14 M22 8 Q40 -6 58 8"/><rect x="8" y="26" width="64" height="26" rx="8"/><rect x="22" y="32" width="36" height="14" rx="4"/></svg>
  <div class="offer-label">High Resolution<br>&amp; Density</div>
</div>
<div class="abs offer-underline"></div>

<section class="abs games"></section>
<div class="abs center games-kicker">Visit Our Theme Park</div>
<h2 class="abs center section-title games-title">Our Games</h2>
<div class="abs rule games-rule"></div>
<div class="abs game" style="left:77px"><div class="game-photo" role="img" aria-label="Player in a dark free roam VR arena with red lights" style="background:linear-gradient(135deg,#1d1420,#5a1c34 55%,#c0305a)"></div><div class="game-name">Roam VR Experiences</div><div class="book">Book Now</div></div>
<div class="abs game" style="left:344px"><div class="game-photo" role="img" aria-label="Two guests seated in blue VR pods" style="background:linear-gradient(180deg,#1a2a8a,#3c56c8 50%,#d8d8e0)"></div><div class="game-name">Strydex</div><div class="book">Book Now</div></div>
<div class="abs game" style="left:612px"><div class="game-photo" role="img" aria-label="Player at a stand alone VR racing station" style="background:linear-gradient(135deg,#2a2a2a,#8a4a3a 50%,#d88a6a)"></div><div class="game-name">Stand alone VR stations</div><div class="book">Book Now</div></div>
<div class="abs game" style="left:879px"><div class="game-photo" role="img" aria-label="Man riding a VR simulator" style="background:linear-gradient(135deg,#d8d8d8,#8a8a96 50%,#3a3a44)"></div><div class="game-name">VR Simulator rides</div><div class="book">Book Now</div></div>

<div class="abs center t-label">Testimonials</div>
<h2 class="abs center section-title t-title">See Our Customers’ Reviews</h2>
<div class="abs rule t-rule"></div>
<p class="abs t-text">Lorem ipsum dolor sit amet, consectetur adipiscing elit, sed do eiusmod tempor incididunt ut labore et.</p>
<div class="abs center t-name">Mara Ellison</div>
<div class="abs avatar" style="left:484px" role="img" aria-label="Customer portrait"></div>
<div class="abs avatar active" style="left:544px" role="img" aria-label="Customer portrait"></div>
<div class="abs avatar" style="left:602px" role="img" aria-label="Customer portrait"></div>
<div class="abs avatar" style="left:663px" role="img" aria-label="Customer portrait"></div>

<footer class="abs footer"></footer>
<div class="abs f-logo"></div>
<div class="abs f-name">Orbit Hopperz VR</div>
<div class="abs f-head" style="left:535px">QUICK LINKS</div>
<ul class="abs f-links"><li>Home</li><li>About</li><li>Games</li><li>Blog</li><li>Testimonials</li><li>Contacts</li></ul>
<div class="abs f-head" style="left:849px">CONTACT US</div>
<div class="abs f-contact">
  <div><svg width="12" height="12" viewBox="0 0 12 12"><rect x="1" y="2" width="10" height="8" rx="1" fill="#fff"/></svg><span>(555) 014 2298 (Phone)</span></div>
  <div><svg width="12" height="12" viewBox="0 0 12 12"><rect x="2" y="1" width="8" height="4" fill="#fff"/><rect x="0" y="5" width="12" height="6" rx="1" fill="#fff"/></svg><span>555 014 2299 (Fax)</span></div>
  <div><svg width="12" height="12" viewBox="0 0 12 12"><rect x="0" y="2" width="12" height="8" fill="#fff"/><path d="M0 2l6 5 6-5" stroke="#1b1b1b" fill="none"/></svg><span>info@orbithopperzvr.com</span></div>
  <div><svg width="12" height="12" viewBox="0 0 12 12"><path d="M6 12 C2 7 2 5 2 4.5 A4 4 0 0 1 10 4.5 C10 5 10 7 6 12Z" fill="#fff"/><circle cx="6" cy="4.5" r="1.5" fill="#1b1b1b"/></svg><span># 88 Nova Crest Lane<br>Brightwater Bay</span></div>
</div>
<div class="abs footbar"></div>
<div class="abs copy">© 2019 Copyrights | All Rights Reserved</div>
<div class="abs social" style="left:980px"></div>
<div class="abs social" style="left:1022px"></div>
<div class="abs social" style="left:1064px"></div>

</body>
</html>
```